Square Business Cards for Our Restaurant / Event Venue

We need square business cards designed for the management team of our event venue and restaurant. On one side of the card should be the the Lantern Hall 7 logo and URL www.lanternhall7.example. On the other side should be the Ember Logo and URL www.emberonfive.example. All employee details should be on the side with Ember logo. There will be a total of 5 cards to be created with the design.

Corinne Baldrath
corinne@lanternhall7.example

main 202.555.4817
direct 202.555.0392

3418 Westbury Lane NW
Washington, DC 20019

```html
<!DOCTYPE html>
<html lang="en">
<head>
<meta charset="utf-8">
<title>Lantern Hall 7 — Square Business Cards</title>
<link rel="stylesheet" href="https://fonts.googleapis.com/css2?family=Open+Sans:ital,wght@0,400;0,700;1,700&display=swap">
<style>
  :root {
    --backdrop: #e8e8e8;
    --card-white: #ffffff;
    --brand-red: #b3191e;
    --ink: #1a1a1a;
    --light: #ffffff;
  }
  * { box-sizing: border-box; margin: 0; padding: 0; }
  html, body { width: 1200px; height: 900px; overflow: hidden; }
  body {
    background: var(--backdrop);
    font-family: "Open Sans", Arial, sans-serif;
    position: relative;
  }
  .card {
    position: absolute;
    top: 202px;
    width: 420px;
    height: 420px;
  }
  .card--front { left: 158px; background: var(--card-white); }
  .card--back  { left: 652px; background: var(--brand-red); color: var(--light); }

  .venue-mark {
    position: absolute;
    left: 0; right: 0;
    top: 140px;
    height: 56px;
    display: flex;
    align-items: center;
    justify-content: center;
    gap: 14px;
  }
  .venue-dot {
    width: 18px;
    height: 18px;
    border-radius: 50%;
    background: var(--brand-red);
  }
  .venue-name {
    color: var(--brand-red);
    font-weight: 400;
    font-size: 40px;
    line-height: 1;
    letter-spacing: 0.5px;
  }
  .front-url {
    position: absolute;
    left: 0; right: 0;
    top: 348px;
    text-align: center;
    font-weight: 700;
    font-style: italic;
    font-size: 17px;
    color: var(--ink);
  }

  .brand-name {
    position: absolute;
    left: 0; right: 0;
    top: 55px;
    text-align: center;
    font-weight: 700;
    font-size: 66px;
    line-height: 1;
    color: var(--light);
  }
  .back-url {
    position: absolute;
    left: 0; right: 0;
    top: 175px;
    text-align: center;
    font-weight: 700;
    font-style: italic;
    font-size: 17px;
  }
  .contact {
    position: absolute;
    left: 48px;
    top: 223px;
    font-size: 17px;
    line-height: 27px;
  }
  .contact-name {
    font-weight: 700;
    font-size: 17px;
    margin-left: 20px;
    margin-bottom: 6px;
    letter-spacing: 0.3px;
  }
  .contact-list { list-style: none; }
  .contact-item {
    display: flex;
    align-items: flex-start;
    font-weight: 700;
    font-style: italic;
  }
  .contact-icon {
    flex: 0 0 14px;
    width: 14px;
    height: 14px;
    margin-top: 7px;
    margin-right: 6px;
  }
  .contact-text { display: block; }
</style>
</head>
<body>
  <section class="card card--front" aria-label="Card front">
    <div class="venue-mark">
      <span class="venue-dot" aria-hidden="true"></span>
      <span class="venue-name">Lantern Hall 7</span>
    </div>
    <p class="front-url">www.lanternhall7.example</p>
  </section>

  <section class="card card--back" aria-label="Card back">
    <p class="brand-name">Ember</p>
    <p class="back-url">www.emberonfive.example</p>
    <div class="contact">
      <p class="contact-name">CORINNE BALDRATH</p>
      <ul class="contact-list">
        <li class="contact-item">
          <svg class="contact-icon" viewBox="0 0 14 14" aria-hidden="true">
            <circle cx="7" cy="7" r="7" fill="#fff"/>
            <rect x="3.5" y="4.5" width="7" height="5" fill="none" stroke="#b3191e" stroke-width="1"/>
            <path d="M3.5 4.5 L7 7.5 L10.5 4.5" fill="none" stroke="#b3191e" stroke-width="1"/>
          </svg>
          <span class="contact-text">corinne@lanternhall7.example</span>
        </li>
        <li class="contact-item">
          <svg class="contact-icon" viewBox="0 0 14 14" aria-hidden="true">
            <circle cx="7" cy="7" r="7" fill="#fff"/>
            <path d="M4.5 4 Q4 7 7 9.5 Q9.5 10.5 10 9.5 L8.8 8.3 L7.8 8.8 Q5.8 7.5 5.3 6.2 L5.8 5.2 Z" fill="#b3191e"/>
          </svg>
          <span class="contact-text">main 202.555.4817<br>direct 202.555.0392</span>
        </li>
        <li class="contact-item">
          <svg class="contact-icon" viewBox="0 0 14 14" aria-hidden="true">
            <circle cx="7" cy="7" r="7" fill="#fff"/>
            <path d="M7 3 A2.8 2.8 0 0 1 9.8 5.8 Q9.8 7.8 7 11 Q4.2 7.8 4.2 5.8 A2.8 2.8 0 0 1 7 3 Z" fill="#b3191e"/>
            <circle cx="7" cy="5.8" r="1.1" fill="#fff"/>
          </svg>
          <span class="contact-text">3418 Westbury Lane NW<br>Washington, DC 20019</span>
        </li>
      </ul>
    </div>
  </section>
</body>
</html>
```